Curriculum company needs new book covers

We are looking for a new design for our book covers to go with our new logo. We are a curriculum company based in Oklahoma, and we create content and assessments to better prepare the students to be successful on the Oklahoma state tests. We need the following:
- Math book cover which needs to stay on a yellow background
-English Language Arts book cover which needs to stay on a royal blue background
The wording on each cover also needs to remain the same although we are open to new fonts. We also want the new logo incorporated into these new book cover designs.
We would like each title (English Language Arts 4) (Math 3) to be at the top of the cover. The final needs to be in a format where we are able to change the subject and the grade level ourselves as we have curriculum in grades K-8.
Photoshop would be the preferred way to receive the images if possible. I am uploading versions of the OLD covers for you to see what we have had for the past 8 years. I am also uploading the painting used on the front; we have the rights to this painting. We would like some designs incorporating the painting in the shape of the state of Oklahoma. We would also like to see some designs that may be new and fresh that do NOT include the painting.
Thank you!
Kindergarten through 8th grade. Administrators or teachers
Education

```html
<!DOCTYPE html>
<html lang="en">
<head>
<meta charset="utf-8">
<title>State Prep – Book Covers</title>
<link rel="stylesheet" href="https://fonts.googleapis.com/css2?family=Exo+2:ital,wght@0,700;0,800;1,700;1,800;1,900&family=Russo+One&family=Montserrat:wght@700&display=swap">
<style>
  :root {
    --page: #ffffff;
    --ela-blue: #3b48a1;
    --ela-blue-deep: #26307a;
    --ela-band: #bcc2e1;
    --math-yellow: #f8c100;
    --math-brown: #8a5a12;
    --math-band: #fde9b3;
    --navy: #0d2f74;
    --accent-yellow: #f7d100;
    --white: #ffffff;
  }
  * { margin: 0; padding: 0; box-sizing: border-box; }
  html, body { width: 1200px; height: 995px; overflow: hidden; background: var(--page); }
  .stage { position: relative; width: 1200px; height: 995px; }

  .cover {
    position: absolute; top: 168px; width: 511px; height: 657px;
    overflow: hidden; background: var(--white);
  }
  .cover--ela { left: 66px; }
  .cover--math { left: 645px; }

  .brand {
    position: absolute; top: 28px; left: 0; width: 100%; height: 34px;
    display: flex; align-items: center; justify-content: center; gap: 10px;
  }
  .brand__square { width: 22px; height: 22px; background: var(--navy); }
  .brand__name {
    font-family: "Montserrat", sans-serif; font-weight: 700; font-size: 20px;
    color: var(--navy); letter-spacing: 0.5px;
  }

  .title-band { position: absolute; top: 91px; left: 0; width: 100%; height: 139px; }
  .art { position: absolute; top: 230px; left: 0; width: 100%; height: 427px; }
  .cover--ela .title-band { background: var(--ela-band); }
  .cover--ela .art { background: radial-gradient(ellipse at 35% 35%, var(--ela-blue-deep) 0%, var(--ela-blue) 65%); }
  .cover--math .title-band { background: var(--math-band); }
  .cover--math .art { background: radial-gradient(ellipse at 35% 35%, var(--math-brown) 0%, var(--math-yellow) 65%); }

  .subject {
    position: absolute; font-family: "Exo 2", sans-serif; font-style: italic;
    font-weight: 800; line-height: 1;
  }
  .subject--ela { left: 85px; top: 126px; font-size: 54px; color: var(--accent-yellow); text-shadow: 3px 3px 0 var(--navy); }
  .subject-sub {
    position: absolute; left: 83px; top: 184px; font-family: "Exo 2", sans-serif;
    font-style: italic; font-weight: 800; font-size: 24px; color: var(--white);
    text-shadow: 2px 2px 0 var(--navy); line-height: 1;
  }
  .subject--math { left: 82px; top: 118px; font-size: 80px; color: var(--navy); font-style: normal; }

  .grade {
    position: absolute; font-family: "Exo 2", sans-serif; font-style: italic;
    font-weight: 900; line-height: 1;
  }
  .grade--ela { left: 318px; top: 96px; font-size: 180px; color: var(--accent-yellow); text-shadow: 5px 4px 0 var(--navy); }
  .grade--math { left: 300px; top: 95px; font-size: 186px; color: var(--navy); text-shadow: 4px 4px 0 var(--white); }

  .series { position: absolute; top: 497px; }
  .series__title {
    font-family: "Russo One", sans-serif; font-size: 50px; line-height: 1;
    letter-spacing: 1px;
  }
  .series__note {
    margin-top: 10px; font-family: "Exo 2", sans-serif; font-style: italic;
    font-weight: 800; font-size: 20px; line-height: 22px; color: var(--white);
  }
  .cover--ela .series { left: 97px; }
  .cover--ela .series__title { color: var(--white); }
  .cover--ela .series__title .series__accent { color: var(--accent-yellow); }
  .cover--math .series { left: 97px; }
  .cover--math .series__title { color: var(--navy); }
  .cover--math .series__title .series__accent { color: var(--white); }
</style>
</head>
<body>
<div class="stage">

  <section class="cover cover--ela">
    <div class="brand"><span class="brand__square"></span><span class="brand__name">BRIGHTPATH LEARNING</span></div>
    <div class="title-band"></div>
    <div class="art" role="img" aria-label="Painting of a shield with feathers and leaves, tinted royal blue"></div>
    <h1 class="subject subject--ela">English</h1>
    <p class="subject-sub">Language Arts</p>
    <p class="grade grade--ela">4</p>
    <div class="series">
      <p class="series__title"><span class="series__accent">STATE</span> PREP</p>
      <p class="series__note">Core Skills<br>Practice<br>Series</p>
    </div>
  </section>

  <section class="cover cover--math">
    <div class="brand"><span class="brand__square"></span><span class="brand__name">BRIGHTPATH LEARNING</span></div>
    <div class="title-band"></div>
    <div class="art" role="img" aria-label="Painting of a shield with feathers and leaves, tinted golden yellow"></div>
    <h1 class="subject subject--math">Math</h1>
    <p class="grade grade--math">3</p>
    <div class="series">
      <p class="series__title"><span class="series__accent">STATE</span> PREP</p>
      <p class="series__note">Core Skills<br>Practice<br>Series</p>
    </div>
  </section>

</div>
</body>
</html>
```